Easy Marinade Labels for Butchery Store

Need a set of labels designed for a Butchery Shop. They will sit in the top left corner of the packets as a triangle (7cm each side). Easy because the only major requirement is the label name and some small text saying "Please ask in store to see spec sheet for ingredients". Extra points for finding a fun way to incorporate the logo and/or images of food (garlic bulbs, chilli, spices ect) to enhance the label. List of Marinade Names below: GarlicPepper Mint & RosemarySatayBBQChilli Plum & GingerSundried Tomato & BasilBuffaloHoney SoyHoi-SinPer PeriSpicy CajunTeriyakiBlack Bean Ive also attached the logo and an example of how the label might sit on a packet of meat. Thanks

Target Market(s)

Butchery Deli Shop Customers

Industry/Entity Type

Food Store

Font styles to use
Serif
Sans Serif
Decorative
Other font styles liked:
• Fun font that isn't a generic Quanderel Font?

Colors

Designer to choose colors to be used in the design.

Requirements
Must have
• Product Name
• Small text saying "Please ask in store to see spec sheet for ingredients"
Nice to have
• Photos of ingredients that would match that type of marinade - Chilli, Garlic, Spices.
• Brava Vell Logo - not essential if it doesn't look good on the label / doesn't fit.

```html
<!DOCTYPE html>
<html lang="en">
<head>
<meta charset="utf-8">
<title>Garlic Pepper Marinade Label</title>
<link rel="stylesheet" href="https://fonts.googleapis.com/css2?family=Caveat+Brush&family=League+Spartan:wght@700;800&display=swap">
<style>
  :root {
    --paper: #ffffff;
    --frame: #f2e51b;
    --spice-dark: #1e0f10;
    --spice-red: #7a1c24;
    --spice-olive: #5a5430;
    --garlic: #d9d2c6;
    --ink: #ffffff;
  }
  * { margin: 0; padding: 0; box-sizing: border-box; }
  html, body {
    width: 1200px; height: 900px; overflow: hidden;
    background: var(--paper);
  }
  .canvas { position: relative; width: 1200px; height: 900px; }
  .label-shape { position: absolute; left: 0; top: 0; }
  .label-text {
    position: absolute; left: 0; top: 0; width: 1200px;
    text-align: center; color: var(--ink);
  }
  .kicker {
    position: absolute; top: 361px; width: 100%;
    font-family: "League Spartan", sans-serif; font-weight: 700;
    font-size: 15px; letter-spacing: 2.5px;
  }
  .product-name {
    position: absolute; top: 385px; width: 100%;
    font-family: "Caveat Brush", cursive;
    font-size: 106px; line-height: 88px; letter-spacing: 3px;
  }
  .notice {
    position: absolute; top: 601px; width: 100%;
    font-family: "League Spartan", sans-serif; font-weight: 800;
    font-size: 22px; letter-spacing: 2px;
  }
</style>
</head>
<body>
<main class="canvas">
  <svg class="label-shape" width="1200" height="900" viewBox="0 0 1200 900">
    <defs>
      <radialGradient id="spice-fill" cx="50%" cy="65%" r="60%">
        <stop offset="0%" stop-color="var(--spice-red)"/>
        <stop offset="55%" stop-color="var(--spice-olive)"/>
        <stop offset="100%" stop-color="var(--spice-dark)"/>
      </radialGradient>
      <linearGradient id="garlic-fill" x1="0" x2="1">
        <stop offset="0%" stop-color="var(--garlic)" stop-opacity="0.55"/>
        <stop offset="30%" stop-color="var(--spice-red)" stop-opacity="0"/>
        <stop offset="70%" stop-color="var(--spice-red)" stop-opacity="0"/>
        <stop offset="100%" stop-color="var(--garlic)" stop-opacity="0.45"/>
      </linearGradient>
    </defs>
    <polygon points="621,170 1097,648 143,648" fill="none" stroke="var(--frame)" stroke-width="10" stroke-linejoin="miter"/>
    <g role="img" aria-label="Photo of mixed peppercorns with garlic cloves">
      <polygon points="621,180 1082,643 158,643" fill="url(#spice-fill)"/>
      <polygon points="621,180 1082,643 158,643" fill="url(#garlic-fill)"/>
    </g>
  </svg>
  <div class="label-text">
    <p class="kicker">MARINATED WITH</p>
    <h1 class="product-name">GARLIC<br>PEPPER</h1>
    <p class="notice">PLEASE ASK IN STORE TO SEE SPEC SHEET FOR INGREDIENTS</p>
  </div>
</main>
</body>
</html>
```